Business Card for a Mortgage Agent (myself)

I need a business card for my new job as Mortgage Agent. The Broker's logo is to be on the card as well as the brokerage License number. Not sure if to include a photo or not. Info to be on card.
Dante Roux
Mortgage Agent
Lic # M47105386
Cell: 905-614-2753
Email: danterouxk.ma@fennmail.com
Web: www.karlvostermortgages.com
TPW Brokerage Lic. # 73918

```html
<!DOCTYPE html>
<html lang="en">
<head>
<meta charset="utf-8">
<title>Dante Roux – Mortgage Agent Business Card</title>
<link rel="stylesheet" href="https://fonts.googleapis.com/css2?family=Montserrat:wght@700&family=Questrial&display=swap">
<style>
  :root {
    --brand-blue: #0557a6;
    --brand-yellow: #fecb0b;
    --card-white: #ffffff;
    --backdrop: #efefef;
    --ink-blue: #124f9c;
  }
  * { margin: 0; padding: 0; box-sizing: border-box; }
  html, body { width: 1200px; height: 1000px; overflow: hidden; }
  body {
    background: var(--backdrop);
    font-family: "Questrial", "Century Gothic", sans-serif;
    position: relative;
  }
  .card { position: absolute; overflow: hidden; }
  .card-front {
    left: 292px; top: 122px; width: 641px; height: 366px;
    background: var(--card-white);
  }
  .card-back {
    left: 286px; top: 544px; width: 654px; height: 373px;
    background: var(--brand-blue);
  }
  .band-svg { position: absolute; left: 0; top: 0; }
  .brokerage-mark {
    position: absolute; left: 40px; top: 160px; width: 240px;
    display: flex; align-items: center; justify-content: center; gap: 12px;
  }
  .brokerage-mark .mark-square {
    width: 28px; height: 28px; background: var(--brand-yellow);
  }
  .brokerage-mark .mark-name {
    font-size: 40px; color: var(--brand-blue); letter-spacing: 10px;
  }
  .brokerage-fullname {
    position: absolute; left: 30px; top: 212px; width: 260px;
    text-align: center; font-size: 12.5px; letter-spacing: 1px;
    color: var(--brand-blue); text-transform: uppercase;
  }
  .brokerage-licence {
    position: absolute; left: 180px; top: 233px;
    font-size: 9px; color: var(--brand-blue);
  }
  .agent-name {
    position: absolute; left: 336px; top: 46px;
    font-family: "Montserrat", "Century Gothic", sans-serif;
    font-weight: 700; font-size: 22px; color: var(--brand-blue);
    display: flex; align-items: center; gap: 6px;
  }
  .agent-name .rule {
    display: inline-block; width: 86px; height: 1.5px; background: var(--brand-blue);
  }
  .agent-title {
    position: absolute; left: 336px; top: 74px;
    font-size: 17px; letter-spacing: 2.4px; color: var(--brand-yellow);
    text-transform: uppercase;
  }
  .contact-list {
    position: absolute; left: 336px; top: 146px; list-style: none;
  }
  .contact-list li {
    display: flex; align-items: center; gap: 7px;
    height: 28px; font-size: 17.5px; color: var(--ink-blue);
  }
  .contact-list svg { width: 14px; height: 14px; flex: none; }
  .licence-text {
    position: absolute; top: 336px; font-size: 16.5px; color: var(--card-white);
  }
  .licence-agent { left: 97px; }
  .licence-brokerage { left: 381px; }
  .back-mark {
    position: absolute; left: 0; top: 150px; width: 100%;
    display: flex; align-items: center; justify-content: center; gap: 16px;
  }
  .back-mark .mark-square { width: 40px; height: 40px; background: var(--card-white); }
  .back-mark .mark-name { font-size: 60px; letter-spacing: 14px; color: var(--card-white); }
</style>
</head>
<body>
  <section class="card card-front" aria-label="Business card front">
    <svg class="band-svg" width="641" height="366" viewBox="0 0 641 366" aria-hidden="true">
      <polygon points="0,0 251,0 232,14 0,14" fill="var(--brand-blue)"/>
      <polygon points="0,330 320,330 353,366 0,366" fill="var(--brand-yellow)"/>
      <polygon points="320,328 641,328 641,366 353,366" fill="var(--brand-blue)"/>
    </svg>

    <div class="brokerage-mark">
      <span class="mark-square"></span>
      <span class="mark-name">TPW</span>
    </div>
    <p class="brokerage-fullname">Tidal Point Wealth Associates</p>
    <p class="brokerage-licence">License #73918</p>

    <h1 class="agent-name">DANTE ROUX <span class="rule"></span></h1>
    <p class="agent-title">Mortgage Agent</p>

    <ul class="contact-list">
      <li>
        <svg viewBox="0 0 16 16" aria-hidden="true"><path fill="var(--brand-yellow)" d="M3.6 1.2l2.3 2.8-1.3 1.8c.9 2 2.5 3.6 4.6 4.6l1.8-1.3 2.8 2.3-1.4 2.6C7 13.6 2.4 9 1 3z"/></svg>
        905-614-2753
      </li>
      <li>
        <svg viewBox="0 0 16 16" aria-hidden="true"><rect x="1" y="3" width="14" height="10" fill="var(--brand-yellow)"/><path d="M1.5 3.5L8 9l6.5-5.5" stroke="#fff" stroke-width="1.2" fill="none"/></svg>
        danterouxk.ma@fennmail.com
      </li>
      <li>
        <svg viewBox="0 0 16 16" aria-hidden="true"><g fill="none" stroke="var(--brand-yellow)" stroke-width="1.4"><circle cx="8" cy="8" r="6.3"/><ellipse cx="8" cy="8" rx="2.6" ry="6.3"/><path d="M1.7 8h12.6"/></g></svg>
        www.karlvostermortgages.com
      </li>
    </ul>

    <p class="licence-text licence-agent">Lic # M47105386</p>
    <p class="licence-text licence-brokerage">TPW Brokerage Lic. # 73918</p>
  </section>

  <section class="card card-back" aria-label="Business card back">
    <div class="back-mark">
      <span class="mark-square"></span>
      <span class="mark-name">TPW</span>
    </div>
  </section>
</body>
</html>
```